FlipCrane is a crypto-arbitrage tool that finds arbitrages between and within exchanges.A logo for the websiteA designer will need to design main page which will describe the project.A subscription page which will have subscription packages. A client portal page where client can set filter types, payment options etc...A Solutions page which will have the actual solutions which flipCrane will calculate. Other pages that have to do with login and subscribing. We need all this to be done as a project with actual color numbers high quality images. ETC... We have attached the current Mock up but designer should have their own input and make it better.
Updates
Project is large and people need time to get it done, please extend by 3 weeks
Need more time to get the project finished right
Target Market(s)
Crypto Traders that are looking to make more money trading
Industry/Entity Type
Finance
Coding
Coded - Design and coding required
Number of Pages Required
5+ page
Colors
Designer to choose colors to be used in the design.
Requirements
Nice to have
- Good animations

```html
<!DOCTYPE html>
<html lang="en">
<head>
<meta charset="utf-8">
<title>FlipCrane – Sign In</title>
<link rel="stylesheet" href="https://fonts.googleapis.com/css2?family=Nunito+Sans:wght@300;400;600&display=swap">
<style>
  :root {
    --teal: #2ee6d6;
    --teal-mid: #45c3df;
    --violet: #7a82e8;
    --card-bg: rgba(240, 248, 252, 0.95);
    --field-border: #5cc3dc;
    --field-fill: rgba(255, 255, 255, 0.12);
    --placeholder: #ffffff;
    --label: #5a6470;
    --check: #4fb9e6;
    --brand-text: #4f8fdc;
    --btn-start: #22e3d6;
    --btn-end: #6f82ec;
    --accent-start: #ff6f7a;
    --accent-end: #f35497;
    --white: #ffffff;
    --rule: rgba(255, 255, 255, 0.75);
  }
  * { box-sizing: border-box; margin: 0; padding: 0; }
  html, body { width: 1200px; height: 709px; overflow: hidden; }
  body {
    font-family: "Nunito Sans", "Segoe UI", sans-serif;
    position: relative;
  }
  .backdrop {
    position: absolute; inset: 0;
    background:
      radial-gradient(ellipse at 45% 55%, rgba(255,255,255,0.10), transparent 60%),
      linear-gradient(100deg, var(--teal) 0%, var(--teal-mid) 45%, var(--violet) 100%);
  }
  .signin-card {
    position: absolute; left: 351px; top: 92px; width: 498px; height: 384px;
    background: var(--card-bg);
    border-radius: 4px;
    box-shadow: 0 4px 18px rgba(0, 60, 90, 0.15);
  }
  .brand {
    position: absolute; left: 0; right: 0; top: 46px;
    display: flex; align-items: center; justify-content: center; gap: 12px;
  }
  .brand-mark {
    width: 22px; height: 22px; background: var(--brand-text); border-radius: 3px;
  }
  .brand-name {
    font-size: 38px; font-weight: 300; letter-spacing: 4px; color: var(--brand-text);
    line-height: 1;
  }
  .field {
    position: absolute; left: 87px; width: 324px; height: 37px;
    border: 1.3px solid var(--field-border); border-radius: 3px;
    background: var(--field-fill);
    display: flex; align-items: center; justify-content: center; gap: 5px;
    color: var(--placeholder); font-size: 13px;
  }
  .field--user { top: 137px; }
  .field--pass { top: 192px; }
  .field svg { width: 12px; height: 12px; }
  .option {
    position: absolute; top: 248px;
    display: flex; align-items: center; gap: 8px;
    font-size: 13px; color: var(--label);
  }
  .option--show { left: 87px; }
  .option--keep { left: 262px; }
  .checkbox {
    width: 19px; height: 19px; border: 1.3px solid var(--check); border-radius: 2px;
    display: flex; align-items: center; justify-content: center;
  }
  .checkbox::after { content: ""; width: 13px; height: 13px; background: var(--check); }
  .btn {
    position: absolute; width: 148px; height: 37px; border-radius: 19px;
    display: flex; align-items: center; justify-content: center;
    color: var(--white); font-size: 13px;
  }
  .btn--signin {
    left: 175px; top: 303px;
    background: linear-gradient(90deg, var(--btn-start), var(--btn-end));
  }
  .divider {
    position: absolute; left: 347px; width: 499px; top: 519px;
    display: flex; align-items: center; gap: 12px;
    color: var(--white); font-size: 13px;
  }
  .divider::before, .divider::after {
    content: ""; flex: 1; height: 1.5px; background: var(--rule);
  }
  .btn--create {
    left: 526px; top: 579px;
    background: linear-gradient(90deg, var(--accent-start), var(--accent-end));
    border: 1px solid rgba(255,255,255,0.8);
  }
</style>
</head>
<body>
  <div class="backdrop" role="img" aria-label="Photo of people reviewing documents at a desk, tinted with a teal-to-violet gradient"></div>

  <main class="signin-card">
    <div class="brand">
      <span class="brand-mark"></span>
      <span class="brand-name">FlipCrane</span>
    </div>

    <div class="field field--user">
      <svg viewBox="0 0 12 12" fill="none" stroke="currentColor" stroke-width="1.2">
        <circle cx="6" cy="6" r="5"/>
        <circle cx="4.3" cy="5" r="0.4" fill="currentColor"/>
        <circle cx="7.7" cy="5" r="0.4" fill="currentColor"/>
        <path d="M3.8 7.4c1.2 1.1 3.2 1.1 4.4 0"/>
      </svg>
      <span>Username</span>
    </div>

    <div class="field field--pass">
      <svg viewBox="0 0 12 12" fill="currentColor">
        <path d="M3.5 5V3.8a2.5 2.5 0 0 1 5 0V5h-1.2V3.8a1.3 1.3 0 0 0-2.6 0V5z"/>
        <rect x="2" y="5" width="8" height="6.5" rx="1"/>
      </svg>
      <span>Password</span>
    </div>

    <label class="option option--show"><span class="checkbox"></span>Show Password</label>
    <label class="option option--keep"><span class="checkbox"></span>Keep me signed</label>

    <div class="btn btn--signin">Sign In</div>
  </main>

  <div class="divider">New Account</div>
  <div class="btn btn--create">Create New Account</div>
</body>
</html>
```